Weather of the Heart Is the Ledger A Novel by Carl Whitby and Martin Holloway

Weather of the Heart Is the Ledger is a business novel about leadership, follower-ship, resilience, and insight.
It follows a high-performing executive whose conventional management tools and techniques stop working during a professional crisis. His transformation does not come from new strategies or tactics, but from a fundamentally different understanding of how mindset shapes performance, decision-making, leadership and follower-ship. Through the course of the book, the executive, his team, and his customers realize that “State of Mind” (healthy psychological functioning) is the horsepower that drives business and life.
This is not a self-help book, textbook, or memoir. It is thoughtful business fiction with philosophical depth.

Introduction/Preface for the novel:
We wrote this book because something profound changed the way we live, work, and lead. Over the course of several decades - across boardrooms, high-stakes corporate challenges, private practice, and moments of quiet personal insight - we began to see a deeper truth about the human experience. It was a truth that, once seen, dramatically improved the quality of our lives, and the lives of the people with whom we worked.
That truth comes from understanding the Three Principles of Mind, Consciousness, and Thought, as discovered and first articulated by the philosopher and theosopher, Edwin Thorley. Though simple, these Principles point to something universally powerful—how all people experience life from the inside out. When understood, they reveal a level of clarity, resilience, and well-being that can transform not only individuals, but entire organizations.
At first, we tried to write a traditional business book—a primer designed to share how understanding the Principles can lead to more grounded, wise, and effective leadership—without the need for techniques or tools. But as we wrote, we found ourselves returning again and again to stories. Real stories. Composite stories. Fictional ones. We realized that the best way to share this understanding wasn’t through frameworks or prescriptive advice. It was through story.
So, we created one big story.
This novel is the result. Though fictional, it is inspired by real patterns, real shifts, and real struggles we’ve lived through and witnessed over decades of work, together and separately. The characters are inventions, but their experiences are familiar. We’ve watched people just like them transform—from confusion to clarity, from fear to resilience, from burnout to wisdom.
Our hope is that this book moves you—not just as a story, but as an experience. We believe that the ideas woven into Owen Castell’s journey can help anyone live with greater ease, purpose, and peace of mind. Whether you lead a Fortune 500 company or a family of five, what’s offered here is for you.
And if something in this story helps you see your own life with fresh eyes, then the book has done its job.
Welcome to the journey.
—Carl & Martin

Target Market(s)

• Senior leaders, executives, and high-potential managers • Business professionals experiencing pressure, burnout, or diminishing returns from traditional leadership approaches • Leadership coaches and organizational consultants • Readers of intelligent, reflective business fiction or non-business people who are interested in what makes people tick — and achieve their highest potential Tone should appeal to serious, experienced professionals, not beginners or hype-seekers.

Industry/Entity Type

• Business / Leadership / Psychology • Business Fiction • Leadership Novel

Font styles to use
Serif

Colors
0054AA
0677BA
7BADD7
CADEEF
E8F1F8

Requirements
Must have
• We are looking for metaphorical representations of: • A fork in the road • A deviation from the conventional path (that makes all the difference) • One element choosing a different direction—not running away, not rebelling, just seeing differently Think quiet insight, not drama. Must-Haves • Clear, legible title at thumbnail size • A visual metaphor for choice or alternate thinking • Professional, credible aesthetic • Obvious that this is fiction (a novel), not a textbook • Clean typography (no clutter)
Nice to have
• • A sense of motion or transition • Minimalist or restrained color palette • One accent element that signifies insight or departure from convention • Timeless design (should still feel current in 5 or 10 years)
Should not have
• • Literal business clichés (gears, ladders, chess pieces, lightbulbs, compasses, eagles) • Stock-photo people in suits • “Hero CEO” imagery • Overly mystical or “woo-woo” visuals • Aggressive, macho, or hustle-culture tone • Anything cartoonish or silly

```html
<!DOCTYPE html>
<html lang="en">
<head>
<meta charset="utf-8">
<title>Weather of the Heart Is the Ledger — Cover</title>
<link rel="stylesheet" href="https://fonts.googleapis.com/css2?family=Crimson+Pro:ital,wght@0,400;0,500;1,400;1,500&display=swap">
<style>
  :root {
    --sky-top: #141c2b;
    --sky-mid: #2c3a52;
    --sky-haze: #6b6a6e;
    --glow: #f4a63c;
    --glow-core: #ffe2a0;
    --ground: #2a2b22;
    --ground-deep: #15150f;
    --cream: #fbf4e4;
    --gold: #f3bb4f;
    --rule: rgba(251, 244, 228, 0.6);
  }
  * { margin: 0; padding: 0; box-sizing: border-box; }
  html, body {
    width: 800px;
    height: 1200px;
    overflow: hidden;
    background: var(--sky-top);
  }
  .cover {
    position: relative;
    width: 800px;
    height: 1200px;
    overflow: hidden;
    font-family: "Crimson Pro", Georgia, serif;
  }
  .cover-scene {
    position: absolute;
    inset: 0;
    width: 800px;
    height: 1200px;
  }
  .title {
    position: absolute;
    left: 0;
    width: 800px;
    text-align: center;
    font-weight: 500;
    line-height: 1;
  }
  .title-top {
    top: 150px;
    font-size: 70px;
    color: var(--cream);
    letter-spacing: 0.2px;
  }
  .title-top em {
    font-style: italic;
    font-weight: 400;
  }
  .title-link {
    position: absolute;
    top: 258px;
    left: 134px;
    width: 534px;
    display: flex;
    align-items: center;
    gap: 26px;
    color: var(--cream);
    font-size: 26px;
    letter-spacing: 4px;
    font-weight: 400;
  }
  .title-link::before,
  .title-link::after {
    content: "";
    flex: 1;
    height: 1px;
    background: var(--rule);
  }
  .title-bottom {
    top: 306px;
    font-size: 96px;
    color: var(--gold);
  }
  .subtitle {
    position: absolute;
    top: 442px;
    left: 0;
    width: 800px;
    text-align: center;
    color: var(--cream);
    font-style: italic;
    font-size: 29px;
    line-height: 42px;
    font-weight: 400;
  }
  .authors {
    position: absolute;
    top: 1068px;
    left: 0;
    width: 800px;
    text-align: center;
    color: var(--gold);
    font-size: 40px;
    letter-spacing: 6px;
    font-weight: 500;
  }
</style>
</head>
<body>
<main class="cover">
  <svg class="cover-scene" viewBox="0 0 800 1200" role="img" aria-label="Photograph of a country road forking in two under a dramatic cloudy sky, with a yellow fork-in-the-road sign at the split and the sun setting on the horizon">
    <defs>
      <linearGradient id="sky" x1="0" y1="0" x2="0" y2="1">
        <stop offset="0" stop-color="var(--sky-top)"/>
        <stop offset="0.35" stop-color="var(--sky-mid)"/>
        <stop offset="0.58" stop-color="var(--sky-haze)"/>
        <stop offset="0.68" stop-color="#c98a3e"/>
        <stop offset="0.72" stop-color="#6b5a35"/>
        <stop offset="0.82" stop-color="var(--ground)"/>
        <stop offset="1" stop-color="var(--ground-deep)"/>
      </linearGradient>
      <radialGradient id="sun" cx="630" cy="680" r="380" gradientUnits="userSpaceOnUse">
        <stop offset="0" stop-color="var(--glow-core)" stop-opacity="0.95"/>
        <stop offset="0.25" stop-color="var(--glow)" stop-opacity="0.7"/>
        <stop offset="1" stop-color="var(--glow)" stop-opacity="0"/>
      </radialGradient>
    </defs>
    <rect width="800" height="1200" fill="url(#sky)"/>
    <rect width="800" height="1200" fill="url(#sun)"/>
  </svg>

  <h1 class="title-block">
    <span class="title title-top">Weather <em>of the</em> Heart</span>
    <span class="title-link">IS THE</span>
    <span class="title title-bottom">Ledger</span>
  </h1>

  <p class="subtitle">A Business Novel about<br>Insight, Resilience, and Transformation</p>

  <p class="authors">WHITBY &amp; MARTIN</p>
</main>
</body>
</html>
```